We Need a Letterhead + Fax Cover Sheet for Kestrel Works

LETTERHEAD:
- Simple letterhead. Please provide an editable .doc file apart from usual Source Files. Logo Files attached for your use.
- Please place our logo on the upper right corner of the page. You may add some sort of graphic, or light colored background (depends on what looks good).
- Footer should include:
Kestrel Works, LLC
418 Wrenfield Ave. Suite 172
Mobile, AL 36619

FAX COVER SHEET:
- Have the logo placed here, should be large, maybe an eight of the page.
- Put:
From:
To:
Phone Number:
Fax Number:

*Still needs some details, will update you because working on the website, etc.

Kestrel Harbor Staffing Services

```html
<!DOCTYPE html>
<html lang="en">
<head>
<meta charset="utf-8">
<title>Kestrel Works Letterhead</title>
<link rel="stylesheet" href="https://fonts.googleapis.com/css2?family=Open+Sans:wght@300;400;700&family=Arimo:wght@700&display=swap">
<style>
  :root {
    --backdrop: #e9e9ea;
    --paper: #ffffff;
    --brand-blue: #1f7fb8;
    --brand-green: #8ea83a;
    --ink: #6a6a6a;
    --ink-soft: #8a8a8a;
    --signature-tone: #d9d9d9;
  }
  * { box-sizing: border-box; margin: 0; padding: 0; }
  html, body {
    width: 1200px; height: 1184px; overflow: hidden;
    background: var(--backdrop);
  }
  .letterhead {
    position: absolute; left: 167px; top: 32px;
    width: 866px; height: 1120px;
    background: var(--paper);
    box-shadow: 0 6px 24px rgba(0,0,0,.18);
    font-family: "Open Sans", sans-serif;
    color: var(--ink);
  }
  .brand-mark {
    position: absolute; top: 62px; right: 70px;
    display: flex; align-items: center; gap: 10px;
    width: 230px;
  }
  .brand-mark__dot {
    flex: none; width: 34px; height: 34px; border-radius: 50%;
    background: var(--brand-blue);
  }
  .brand-mark__name {
    font-family: "Open Sans", sans-serif; font-weight: 700;
    font-size: 17px; line-height: 1.25; color: var(--brand-blue);
    text-transform: uppercase;
  }
  .letter-body {
    position: absolute; left: 112px; top: 360px; width: 620px;
    font-size: 14px; font-weight: 300; line-height: 1.55;
  }
  .letter-body .salutation { margin-bottom: 18px; }
  .letter-body p.paragraph { margin-bottom: 22px; text-align: justify; }
  .sign-off { margin-top: 8px; }
  .signature {
    display: block; width: 120px; height: 70px; margin: 22px 0 22px 20px;
    background: var(--signature-tone); border-radius: 4px;
  }
  .signatory { font-size: 13px; line-height: 1.4; color: var(--ink-soft); margin-left: 20px; }
  .footer-band {
    position: absolute; left: 0; right: 0; bottom: 0; height: 66px;
    background: var(--brand-blue);
    border-top: 4px solid var(--brand-green);
    display: flex; align-items: center; justify-content: flex-end;
    padding-right: 52px;
    font-family: "Arimo", sans-serif; font-weight: 700;
    font-size: 14px; letter-spacing: 1.6px; color: var(--paper);
  }
  .footer-band .company { color: var(--brand-green); text-transform: uppercase; margin-right: 8px; }
</style>
</head>
<body>
  <main class="letterhead">
    <div class="brand-mark">
      <span class="brand-mark__dot"></span>
      <span class="brand-mark__name">Kestrel Harbor Staffing Services</span>
    </div>

    <section class="letter-body">
      <p class="salutation">Dear customer,</p>
      <p class="paragraph">Lorem ipsum dolor sit amet, consectetur adipisicing elit, sed do eiusmod tempor incididunt ut labore et dolore magna aliqua. Ut enim ad minim veniam, quis nostrud exercitation ullamco laboris nisi ut aliquip ex ea commodo consequat. Duis aute irure dolor in reprehenderit in voluptate velit esse cillum dolore eu fugiat nulla pariatur. Excepteur sint occaecat cupidatat non proident, sunt in culpa qui officia deserunt mollit anim id est laborum.</p>
      <p class="paragraph">Lorem ipsum dolor sit amet, consectetur adipisicing elit, sed do eiusmod tempor incididunt ut labore et dolore magna aliqua. Ut enim ad minim veniam, quis nostrud exercitation ullamco laboris nisi ut aliquip ex ea commodo consequat. Duis aute irure dolor in reprehenderit in voluptate velit esse cillum dolore eu fugiat nulla pariatur. Excepteur sint occaecat cupidatat non proident, sunt in culpa qui officia deserunt mollit anim id est laborum.</p>
      <p class="paragraph">Lorem ipsum dolor sit amet, consectetur adipisicing elit, sed do eiusmod tempor incididunt ut labore et dolore magna aliqua. Ut enim ad minim veniam, quis nostrud exercitation ullamco laboris nisi ut aliquip ex ea commodo consequat. Duis aute irure dolor in reprehenderit in voluptate velit esse cillum dolore eu fugiat nulla pariatur. Excepteur sint occaecat cupidatat non proident, sunt in culpa qui officia deserunt mollit anim id est laborum.</p>
      <p class="sign-off">Yours Sincerely,</p>
      <span class="signature" role="img" aria-label="Handwritten signature of the General Director"></span>
      <p class="signatory">Marcus Hale<br>General Director</p>
    </section>

    <footer class="footer-band">
      <span class="company">Kestrel Works, LLC</span>
      <span class="address">- 418 Wrenfield Ave. Suite 172, Mobile, AL 36619</span>
    </footer>
  </main>
</body>
</html>
```